Desk Allies Business Card

Contact Information for Business Card

Janne Voutilainen
Managing Director

3/47 Brindle Street Kelvale ACT 2914

Tel: +61 02 6257 3140
Mob: +61 0427 315 846

Email: janne@deskallies.com.au
Web: www.deskallies.com.au

Colors

Designer to choose colors to be used in the design.

Requirements
Must have
• Logo, Name, Title, Address, Telephone, Mobile, Email Address and Website
• "Desk Ally International Pty Ltd"

```html
<!DOCTYPE html>
<html lang="en">
<head>
<meta charset="utf-8">
<title>Desk Allies Business Card</title>
<link href="https://fonts.googleapis.com/css2?family=Montserrat:wght@400;500;600&display=swap" rel="stylesheet">
<style>
  :root {
    --backdrop: #a7b8c3;
    --card-dark: #262626;
    --card-light: #f1f1ef;
    --brand-blue: #2f7fd1;
    --ink-dark: #2a2a2a;
    --ink-muted: #6b6b6b;
    --ink-light: #d9d9d9;
    --emboss: #dcdcda;
  }
  * { box-sizing: border-box; margin: 0; padding: 0; }
  html, body {
    width: 1200px; height: 978px; overflow: hidden;
    background: var(--backdrop);
    font-family: "Montserrat", sans-serif;
  }
  .sheet {
    width: 1200px; height: 978px;
    display: flex; align-items: center; justify-content: center; gap: 60px;
  }
  .card {
    position: relative;
    width: 520px; height: 318px;
    border-bottom: 4px solid var(--brand-blue);
    border-radius: 3px;
    box-shadow: 0 18px 40px rgba(40, 60, 75, 0.25);
  }
  /* Front */
  .card--front { background: var(--card-dark); color: var(--ink-light); }
  .brand { position: absolute; left: 60px; top: 96px; }
  .brand__line { display: flex; align-items: center; gap: 16px; }
  .brand__dot {
    width: 42px; height: 42px; border-radius: 50%;
    background: var(--brand-blue);
  }
  .brand__name {
    font-size: 34px; font-weight: 500; letter-spacing: 1px;
    color: var(--brand-blue); text-transform: uppercase;
  }
  .brand__tagline {
    margin: 4px 0 0 58px;
    font-size: 10.5px; letter-spacing: 3px; color: #b9b9b9;
    text-transform: uppercase;
  }
  .company { position: absolute; left: 60px; top: 200px; font-size: 12.5px; line-height: 24px; }
  .company__web .accent { color: var(--brand-blue); }
  /* Back */
  .card--back { background: var(--card-light); color: var(--ink-dark); }
  .person { position: absolute; left: 50px; top: 44px; }
  .person__name { font-size: 22px; font-weight: 500; color: var(--brand-blue); }
  .person__title { font-size: 13px; color: var(--ink-muted); margin-top: 2px; }
  .contact { position: absolute; font-size: 12.5px; line-height: 17px; }
  .contact dt { font-weight: 600; }
  .contact dd { margin-bottom: 8px; }
  .contact--phones { left: 50px; top: 124px; }
  .contact--address { left: 220px; top: 200px; }
  .emboss-mark {
    position: absolute; right: 36px; bottom: 40px;
    width: 64px; height: 64px; border-radius: 50%;
    border: 5px solid var(--emboss);
  }
</style>
</head>
<body>
<main class="sheet">
  <section class="card card--front" aria-label="Card front">
    <div class="brand">
      <div class="brand__line">
        <span class="brand__dot"></span>
        <span class="brand__name">Desk Allies</span>
      </div>
      <p class="brand__tagline">Ergonomic Workspace Solutions</p>
    </div>
    <div class="company">
      <p class="company__legal">Desk Ally International Pty Ltd</p>
      <p class="company__web">www.<span class="accent">deskallies</span>.com.au</p>
    </div>
  </section>

  <section class="card card--back" aria-label="Card back">
    <div class="person">
      <p class="person__name">Janne Voutilainen</p>
      <p class="person__title">Managing Director</p>
    </div>
    <dl class="contact contact--phones">
      <dt>mobile</dt><dd>+61 0427 315 846</dd>
      <dt>tel</dt><dd>+61 02 6257 3140</dd>
    </dl>
    <dl class="contact contact--address">
      <dd>3/47 Brindle Street<br>Kelvale ACT 2914</dd>
      <dt>email</dt><dd>janne@deskallies.com.au</dd>
    </dl>
    <span class="emboss-mark" aria-hidden="true"></span>
  </section>
</main>
</body>
</html>
```